CalmHarbor Homepage and Landing Pages

Please see detailed brief.

CalmHarbor is Australia’s newest online therapy and mental health service. We allow patients from across australia to connect with Mental health practitioners from across Australia. Our mission is to remove the friction in gaining support for mental health related issues.

Number of Pages Required

1 page

Font styles to use
Sans Serif

Colors
33a6d7
0293ce
3277b5
0255a3
acd136
9bcb3c

Requirements
Must have
• Please see detailed brief.
Nice to have
• Please see detailed brief
Should not have

```html
<!DOCTYPE html>
<html lang="en">
<head>
<meta charset="utf-8">
<title>CalmHarbor Homepage and Modals</title>
<link rel="stylesheet" href="https://fonts.googleapis.com/css2?family=Roboto:wght@300;400;500;700&display=swap">
<style>
:root{
  --board:#0f9cf1;
  --brand:#0757d4;
  --brand-dark:#0347b4;
  --cyan:#17a4f4;
  --white:#ffffff;
  --ink:#1d2430;
  --muted:#6b7280;
  --line:#c9ced6;
  --navy:#0c2a66;
  --dim-nav:#737a85;
}
*{box-sizing:border-box;margin:0;padding:0}
html,body{width:1200px;height:1200px;overflow:hidden}
body{background:var(--board);font-family:'Roboto',sans-serif;color:var(--ink);position:relative}
.abs{position:absolute}
.center{text-align:center}
.page{position:absolute;left:101px;top:0;width:401px;height:1200px;background:var(--white);overflow:hidden}
.topbar{left:0;top:0;width:401px;height:12px;background:var(--brand)}
.topbar span{position:absolute;top:3.5px;font-size:2.6px;color:#dfe8ff}
.dot-icon{position:absolute;width:4px;height:4px;border-radius:50%;background:#dfe8ff;top:4px}
.nav{left:0;top:12px;width:401px;height:19px;background:var(--white)}
.logo{position:absolute;font-weight:300;color:var(--brand);white-space:nowrap;display:flex;align-items:center}
.logo i{display:inline-block;border-radius:50%;background:currentColor;margin-right:3px}
.nav a{position:absolute;top:8px;font-size:3.2px;font-weight:500;color:var(--ink);text-decoration:none;white-space:nowrap}
.nav a.active{color:var(--brand)}
.btn{position:absolute;display:flex;align-items:center;justify-content:center;color:var(--white);font-weight:500;white-space:nowrap;background:var(--brand)}
.btn.cyan{background:var(--cyan)}
.hero{left:0;top:31px;width:401px;height:199px;background:linear-gradient(100deg,#c4cbcf 0%,#e7ecee 40%,#d9dfe2 70%,#b8c0c4 100%)}
.hero-title{left:60px;width:186px;top:72px;font-size:16px;font-weight:500;color:var(--brand)}
.hero-text{left:50px;width:206px;top:92px;font-size:5px;line-height:6.4px;color:var(--brand)}
.arrow{position:absolute;width:6px;height:6px;border-top:1.5px solid var(--brand);border-left:1.5px solid var(--brand)}
.arrow.l{transform:rotate(-45deg)}
.arrow.r{transform:rotate(135deg)}
.dots{display:flex;gap:4px}
.dots b{width:4px;height:4px;border-radius:50%;background:#6a7280}
.dots b:first-child{background:var(--brand)}
.chat{background:#35b7f2;border-radius:2px;display:flex;align-items:center;padding-left:12px;font-size:2.4px;color:var(--white)}
.finder{left:21px;top:205px;width:359px;height:47px;background:var(--brand)}
.finder h3{position:absolute;left:7px;top:8px;font-size:6.5px;font-weight:500;color:var(--white)}
.field{position:absolute;top:23.5px;height:15.5px;background:var(--white);font-size:4.4px;color:#4a5160;display:flex;align-items:center;padding-left:5px}
.field svg{position:absolute;right:5px;top:4px}
.section-title{position:absolute;font-weight:500;color:var(--brand);white-space:nowrap}
.body-text{position:absolute;font-size:4.6px;line-height:5.9px;color:var(--muted)}
.device{position:absolute;border-radius:9px;background:linear-gradient(160deg,#5d7d3c,#c9c2b8 55%,#8a6a63);border:2px solid #1b1b1b}
.band{left:0;top:422px;width:401px;height:148px;background:var(--brand)}
.team-card{position:absolute;top:632px;width:111px;height:148px;border-radius:7px;background:var(--white);box-shadow:0 1px 4px rgba(0,0,0,.25);overflow:hidden}
.team-card.featured{background:var(--brand)}
.avatar{position:absolute;left:32px;top:25px;width:46px;height:46px;border-radius:50%;background:linear-gradient(160deg,#2a86ea,#8fc2f2)}
.team-card .name{position:absolute;left:0;width:111px;top:81px;font-size:5.6px;text-align:center;color:var(--ink)}
.team-card .addr{position:absolute;left:0;width:111px;top:90px;font-size:4.4px;text-align:center;color:var(--muted)}
.team-card.featured .name,.team-card.featured .addr{color:var(--white)}
.tag{position:absolute;left:35px;top:107px;width:41px;height:9px;background:var(--brand);color:var(--white);font-size:3.2px;display:flex;align-items:center;justify-content:center}
.featured .tag{background:var(--cyan)}
.card-foot{position:absolute;left:0;bottom:0;width:111px;height:15px;display:flex;border-top:1px solid #d8dbe0}
.card-foot span{flex:1;display:flex;align-items:center;justify-content:center;font-size:2.8px;color:#4a5160}
.card-foot span+span{border-left:1px solid #d8dbe0}
.featured .card-foot{border-top-color:#3b7ee4}
.featured .card-foot span{color:var(--white)}
.featured .card-foot span+span{border-left-color:#3b7ee4}
.map{left:0;top:803px;width:401px;height:202px;background:linear-gradient(135deg,#2f6fd6,#1f62cf 55%,#3a7ade)}
.contact-card{left:21px;top:922px;width:359px;height:166px;background:var(--white);box-shadow:0 2px 6px rgba(0,0,0,.2)}
.contact-card h4{position:absolute;font-size:5.8px;font-weight:500}
.flabel{position:absolute;font-size:3.3px;color:#8b919b}
.fline{position:absolute;height:0;border-top:.8px solid var(--line)}
.info{position:absolute;left:239px;top:0;width:120px;height:166px;background:var(--cyan)}
.info .row{position:absolute;left:17px;display:flex;align-items:center;gap:8px;font-size:3.4px;color:var(--white)}
.social{position:absolute;width:5px;height:5px;border-radius:50%;background:var(--white)}
.footer{left:0;top:1111px;width:401px;height:77px;background:var(--brand)}
.footer h5{position:absolute;top:19px;font-size:4.6px;font-weight:500;color:var(--white)}
.footer p{position:absolute;width:56px;font-size:2.6px;line-height:3.3px;color:#d6e2ff}
.to-top{left:387px;top:1174px;width:14px;height:14px;background:var(--cyan)}
.board-label{position:absolute;left:599px;width:503px;text-align:center;font-weight:400;color:#0a0f1a;letter-spacing:1px}
.screen{position:absolute;left:599px;width:503px;height:283px;overflow:hidden;background:linear-gradient(100deg,#80878f,#a7adb3 45%,#8d949b)}
.s-top{left:0;top:0;width:503px;height:14px;background:var(--navy)}
.s-top span{position:absolute;top:5px;font-size:2.8px;color:#8fa2c8}
.s-top .dot-icon{background:#8fa2c8;top:5px}
.s-nav{left:0;top:14px;width:503px;height:26px;background:var(--dim-nav)}
.s-nav a{position:absolute;top:11px;font-size:3.6px;font-weight:500;color:#1c2230;text-decoration:none;white-space:nowrap}
.s-nav a.active{color:#0a3a96}
.s-finder{left:27px;top:257px;width:450px;height:26px;background:#0a2f7a}
.s-finder span{position:absolute;left:9px;top:9px;font-size:8px;font-weight:500;color:#8e9bb5}
.modal{left:65px;top:50px;width:373px;height:186px;background:var(--white);border-radius:7px;overflow:hidden}
.modal .side{position:absolute;left:0;top:0;width:202px;height:186px;background:var(--brand)}
.modal .hello{position:absolute;left:14px;top:13px;font-size:10px;line-height:12.5px;font-weight:500;color:var(--white)}
.modal .photo{position:absolute;left:40px;top:42px;width:118px;height:144px;background:linear-gradient(180deg,rgba(255,255,255,.08),rgba(255,255,255,.32))}
.mtitle{position:absolute;left:202px;width:171px;text-align:center;font-weight:500;color:var(--brand)}
.msub{position:absolute;left:202px;width:171px;text-align:center;font-size:4.5px;color:#3b414c}
.close{position:absolute;left:425px;width:18px;height:18px;border-radius:50%;background:var(--brand);border:1.2px solid var(--white)}
</style>
</head>
<body>

<main class="page">
  <div class="abs topbar">
    <div class="dot-icon" style="left:21px"></div><span style="left:27px">+61 400 555 010</span>
    <div class="dot-icon" style="left:74px"></div><span style="left:80px">HELLO@CALMHARBOR.EXAMPLE</span>
    <div class="dot-icon" style="left:319px"></div><div class="dot-icon" style="left:339px"></div><div class="dot-icon" style="left:358px"></div><div class="dot-icon" style="left:377px"></div>
  </div>
  <nav class="abs nav">
    <div class="logo" style="left:22px;top:4px;font-size:8.5px"><i style="width:5px;height:5px"></i>CalmHarbor</div>
    <a class="active" style="left:96px">FOR PRACTITIONER</a>
    <a style="left:148px">HOW IT WORKS</a>
    <a style="left:193px">MEET OUR TEAM</a>
    <a style="left:240px">CONTACT</a>
    <a style="left:302px">○ LOGIN</a>
    <span class="btn" style="left:336px;top:4px;width:44px;height:11px;font-size:3.2px">PATIENT SIGN IN</span>
  </nav>

  <section class="abs hero" role="img" aria-label="Smiling female doctor in a white coat presenting with an open hand, clinic interior behind"></section>
  <h1 class="abs hero-title center">WE'RE IN BETA!</h1>
  <p class="abs hero-text center">CalmHarbor provides on-demand access to a range of psychologists &amp; personal wellness professionals from across Australia.<br>Book your online appointment in minutes, 24/7.</p>
  <span class="btn" style="left:126px;top:122px;width:56px;height:13px;font-size:3.6px">FIND A PRACTITIONER</span>
  <span class="arrow l" style="left:23px;top:122px"></span>
  <span class="arrow r" style="left:373px;top:124px"></span>
  <div class="abs dots" style="left:146px;top:191px"><b></b><b></b><b></b></div>
  <div class="abs chat" style="left:327px;top:196px;width:52px;height:9px">Let's chat</div>

  <section class="abs finder">
    <h3>I NEED TO FIND</h3>
    <div class="field" style="left:7px;width:94px">DOCTOR
      <svg width="6" height="7" viewBox="0 0 6 7"><circle cx="3" cy="2" r="1.6" fill="#4a5160"/><path d="M0 7a3 3 0 0 1 6 0z" fill="#4a5160"/></svg></div>
    <div class="field" style="left:104px;width:94px">SPECIALITY
      <svg width="7" height="7" viewBox="0 0 7 7"><path d="M1 1v3a2 2 0 0 0 4 0V1M5 4h1.5" stroke="#4a5160" stroke-width=".7" fill="none"/></svg></div>
    <div class="field" style="left:202px;width:94px">LOCATION
      <svg width="5" height="7" viewBox="0 0 5 7"><path d="M2.5 7C.5 4 0 3.2 0 2.5a2.5 2.5 0 0 1 5 0c0 .7-.5 1.5-2.5 4.5z" fill="#4a5160"/><circle cx="2.5" cy="2.5" r=".9" fill="#fff"/></svg></div>
    <span class="btn cyan" style="left:299px;top:23.5px;width:53px;height:15.5px;font-size:4.6px;gap:3px">
      <svg width="5" height="5" viewBox="0 0 5 5"><circle cx="2" cy="2" r="1.5" stroke="#fff" stroke-width=".7" fill="none"/><path d="M3.1 3.1 4.6 4.6" stroke="#fff" stroke-width=".7"/></svg>SEARCH</span>
  </section>

  <h2 class="section-title" style="left:34px;width:182px;text-align:center;top:295px;font-size:10.5px">OUR MISSION IS SIMPLE</h2>
  <p class="body-text center" style="left:40px;width:170px;top:314px">We want to break down the barriers in receiving effective treatment and care for anxiety, stress and mental health related issues.</p>
  <span class="btn" style="left:92px;top:347px;width:65px;height:14px;font-size:4.8px">HOW IT WORKS?</span>
  <div class="device" style="left:252px;top:264px;width:70px;height:141px" role="img" aria-label="Smartphone showing a video call with a female practitioner"></div>
  <div class="device" style="left:296px;top:305px;width:50px;height:99px" role="img" aria-label="Second smartphone showing the same practitioner"></div>

  <section class="abs band">
    <div class="device" style="left:71px;top:14px;width:59px;height:120px" role="img" aria-label="Smartphone showing a female practitioner outdoors"></div>
    <h2 class="section-title" style="left:166px;width:200px;text-align:center;top:25px;font-size:10px;color:var(--white)">FIND THE HELP YOU NEED</h2>
    <p class="body-text center" style="left:166px;width:200px;top:47px;color:#e1eaff">Book an appointment with one of our highly qualified, licensed practitioners. The consultation can be conducted from wherever you feel most comfortable.</p>
    <p class="body-text center" style="left:166px;width:200px;top:71px;color:#e1eaff">No travel. No Clinics.</p>
    <span class="btn cyan" style="left:228px;top:100px;width:78px;height:16px;font-size:5px">FIND THE PRACTITIONER</span>
  </section>

  <h2 class="section-title" style="left:0;width:401px;text-align:center;top:580px;font-size:10px">OUR TEAM</h2>
  <p class="body-text center" style="left:50px;width:300px;top:601px">Our Practitioners are what makes CalmHarbor tick. However behind every great product is a hardworking team ensuring that CalmHarbor can deliver the highest quality of service</p>

  <article class="team-card featured" style="left:21px">
    <div class="avatar" role="img" aria-label="Portrait photo of a practitioner"></div>
    <div class="name">Dr. Milo</div><div class="addr">48 Harbour Lane, Unit 12</div>
    <span class="tag">ANXIETY</span>
    <div class="card-foot"><span>▢ AVAILABILITY</span><span>☏ BOOK NOW</span></div>
  </article>
  <article class="team-card" style="left:145px">
    <div class="avatar" role="img" aria-label="Portrait photo of a practitioner"></div>
    <div class="name">Dr. Milo</div><div class="addr">48 Harbour Lane, Unit 12</div>
    <span class="tag">ANXIETY</span>
    <div class="card-foot"><span>▢ AVAILABILITY</span><span>☏ BOOK NOW</span></div>
  </article>
  <article class="team-card" style="left:269px">
    <div class="avatar" role="img" aria-label="Portrait photo of a practitioner"></div>
    <div class="name">Dr. Milo</div><div class="addr">48 Harbour Lane, Unit 12</div>
    <span class="tag">ANXIETY</span>
    <div class="card-foot"><span>▢ AVAILABILITY</span><span>☏ BOOK NOW</span></div>
  </article>

  <section class="abs map" role="img" aria-label="Blue-tinted city street map behind the contact section"></section>
  <h2 class="section-title" style="left:0;width:401px;text-align:center;top:845px;font-size:10px;color:var(--white)">GET IN TOUCH</h2>
  <p class="body-text center" style="left:50px;width:300px;top:863px;color:var(--white)">Our Practitioners are what makes CalmHarbor tick. However behind every great product is a hardworking team ensuring that CalmHarbor can deliver the highest quality of service</p>

  <section class="abs contact-card">
    <h4 style="left:15px;top:12px;color:var(--brand)">SEND US MESSAGE</h4>
    <span class="flabel" style="left:15px;top:40px">FIRST NAME</span><span class="fline" style="left:15px;top:52px;width:68px"></span>
    <span class="flabel" style="left:122px;top:40px">LAST NAME</span><span class="fline" style="left:122px;top:52px;width:68px"></span>
    <span class="flabel" style="left:15px;top:73px">PHONE</span><span class="fline" style="left:15px;top:88px;width:68px"></span>
    <span class="flabel" style="left:122px;top:73px">EMAIL</span><span class="fline" style="left:122px;top:88px;width:68px"></span>
    <span class="flabel" style="left:15px;top:116px">MESSAGE</span><span class="fline" style="left:15px;top:144px;width:165px"></span>
    <svg class="abs" style="left:182px;top:135px" width="19" height="19" viewBox="0 0 19 19"><circle cx="9.5" cy="9.5" r="9.5" fill="#0d6fe0"/><path d="M6 5.5 14 9.5 6 13.5 7.5 9.5z" fill="#7fd3ff"/></svg>
    <div class="info">
      <h4 style="left:14px;top:12px;color:var(--white)">CONTACT INFORMATION</h4>
      <div class="row" style="top:40px"><svg width="5" height="7" viewBox="0 0 5 7"><path d="M2.5 7C.5 4 0 3.2 0 2.5a2.5 2.5 0 0 1 5 0c0 .7-.5 1.5-2.5 4.5z" fill="#fff"/></svg>48 HARBOUR LANE, UNIT 12</div>
      <div class="row" style="top:67px"><svg width="6" height="5" viewBox="0 0 6 5"><rect width="6" height="5" fill="#fff"/><path d="M0 0 3 2.5 6 0" stroke="#17a4f4" stroke-width=".6" fill="none"/></svg>HELLO@CALMHARBOR.EXAMPLE</div>
      <div class="row" style="top:94px"><svg width="6" height="6" viewBox="0 0 6 6"><path d="M1 0 2.3 1.6 1.6 2.5A4 4 0 0 0 3.5 4.4l.9-.7L6 5 5 6A5 5 0 0 1 0 1z" fill="#fff"/></svg>03 5550 1234</div>
      <span class="social" style="left:15px;top:141px"></span><span class="social" style="left:41px;top:141px"></span><span class="social" style="left:67px;top:141px"></span><span class="social" style="left:92px;top:141px"></span>
    </div>
  </section>

  <footer class="abs footer">
    <div class="logo" style="left:22px;top:14px;font-size:10px;color:#3aa6f5"><i style="width:5px;height:5px"></i>CalmHarbor</div>
    <h5 style="left:130px">LATEST POST</h5><h5 style="left:222px">HEAD OFFICE</h5><h5 style="left:314px">QUICK LINES</h5>
    <p style="left:130px;top:28px">Our practitioners help you find calm, care and support every day, wherever you are.</p>
    <p style="left:222px;top:28px">Our practitioners help you find calm, care and support every day, wherever you are.</p>
    <p style="left:314px;top:28px">Our practitioners help you find calm, care and support every day, wherever you are.</p>
    <p style="left:130px;top:56px">Fresh notes from our clinical team this week.</p>
    <p style="left:222px;top:56px">Fresh notes from our clinical team this week.</p>
    <p style="left:314px;top:56px">Fresh notes from our clinical team this week.</p>
  </footer>
  <div class="abs to-top"><span class="arrow" style="left:5px;top:6px;width:4px;height:4px;border-color:#fff;transform:rotate(45deg);border-width:1px"></span></div>
</main>

<h2 class="board-label" style="top:28px;font-size:31px">LOGIN</h2>
<section class="screen" style="top:108px" aria-label="Login modal over homepage">
  <div class="abs s-top">
    <div class="dot-icon" style="left:27px"></div><span style="left:35px">+61 400 555 010</span>
    <div class="dot-icon" style="left:93px"></div><span style="left:103px">HELLO@CALMHARBOR.EXAMPLE</span>
    <div class="dot-icon" style="left:401px"></div><div class="dot-icon" style="left:425px"></div><div class="dot-icon" style="left:449px"></div><div class="dot-icon" style="left:472px"></div>
  </div>
  <nav class="abs s-nav">
    <div class="logo" style="left:28px;top:6px;font-size:11px;color:#1c2a4a"><i style="width:6px;height:6px"></i>CalmHarbor</div>
    <a class="active" style="left:121px">FOR PRACTITIONER</a><a style="left:186px">HOW IT WORKS</a><a style="left:242px">MEET OUR TEAM</a><a style="left:301px">CONTACT</a><a style="left:379px">○ LOGIN</a>
    <span class="btn" style="left:421px;top:6px;width:55px;height:14px;font-size:3.8px;background:#0a2f7a;color:#a9b7d4">PATIENT SIGN IN</span>
  </nav>
  <span class="arrow l" style="left:29px;top:156px;border-color:#0a3a96"></span>
  <span class="arrow r" style="left:469px;top:158px;border-color:#0a3a96"></span>
  <div class="abs dots" style="left:184px;top:241px"><b></b><b></b><b></b></div>
  <div class="abs chat" style="left:411px;top:246px;width:64px;height:11px;background:#1e5f85;color:#8fb0c8">Let's chat</div>
  <div class="abs s-finder"><span>I NEED TO FIND</span></div>
  <div class="abs modal">
    <div class="side">
      <p class="hello">HELLO!<br>WE ARE FROM CALMHARBOR</p>
      <div class="photo" role="img" aria-label="Photo of a smiling male doctor in a white coat giving a thumbs up"></div>
    </div>
    <h3 class="mtitle" style="top:28px;font-size:8px">LOGIN</h3>
    <p class="msub" style="top:40px">Book your online appointment in minutes, 24/7.</p>
    <span class="flabel" style="left:218px;top:69px">USERNAME</span><span class="fline" style="left:218px;top:80px;width:138px"></span>
    <span class="flabel" style="left:218px;top:91px">PASSWORD</span><span class="fline" style="left:218px;top:105px;width:138px"></span>
    <span class="btn" style="left:218px;top:125px;width:138px;height:11px;font-size:3.4px;gap:8px">▶ CONTINUE</span>
  </div>
  <div class="close" style="top:43px"><svg width="16" height="16" viewBox="0 0 16 16"><path d="M4.5 4.5 11.5 11.5M11.5 4.5 4.5 11.5" stroke="#fff" stroke-width="1.4"/></svg></div>
</section>

<h2 class="board-label" style="top:436px;font-size:31px">REGISTER</h2>
<section class="screen" style="top:516px" aria-label="Register modal over homepage">
  <div class="abs s-top">
    <div class="dot-icon" style="left:27px"></div><span style="left:35px">+61 400 555 010</span>
    <div class="dot-icon" style="left:93px"></div><span style="left:103px">HELLO@CALMHARBOR.EXAMPLE</span>
    <div class="dot-icon" style="left:401px"></div><div class="dot-icon" style="left:425px"></div><div class="dot-icon" style="left:449px"></div><div class="dot-icon" style="left:472px"></div>
  </div>
  <nav class="abs s-nav">
    <div class="logo" style="left:28px;top:6px;font-size:11px;color:#1c2a4a"><i style="width:6px;height:6px"></i>CalmHarbor</div>
    <a class="active" style="left:121px">FOR PRACTITIONER</a><a style="left:186px">HOW IT WORKS</a><a style="left:242px">MEET OUR TEAM</a><a style="left:301px">CONTACT</a><a style="left:379px">○ LOGIN</a>
    <span class="btn" style="left:421px;top:6px;width:55px;height:14px;font-size:3.8px;background:#0a2f7a;color:#a9b7d4">PATIENT SIGN IN</span>
  </nav>
  <span class="arrow l" style="left:29px;top:156px;border-color:#0a3a96"></span>
  <span class="arrow r" style="left:469px;top:158px;border-color:#0a3a96"></span>
  <div class="abs dots" style="left:184px;top:241px"><b></b><b></b><b></b></div>
  <div class="abs chat" style="left:411px;top:246px;width:64px;height:11px;background:#1e5f85;color:#8fb0c8">Let's chat</div>
  <div class="abs s-finder"><span>I NEED TO FIND</span></div>
  <div class="abs modal">
    <div class="side">
      <p class="hello">HELLO!<br>WE ARE FROM CALMHARBOR</p>
      <div class="photo" role="img" aria-label="Photo of a smiling male doctor in a white coat giving a thumbs up"></div>
    </div>
    <h3 class="mtitle" style="top:13px;font-size:8px">REGISTER</h3>
    <p class="msub" style="top:23px">Book your online appointment in minutes, 24/7.</p>
    <span class="flabel" style="left:218px;top:40px">FIRST NAME</span><span class="fline" style="left:218px;top:50px;width:55px"></span>
    <span class="flabel" style="left:307px;top:40px">LAST NAME</span><span class="fline" style="left:307px;top:50px;width:55px"></span>
    <span class="flabel" style="left:218px;top:63px">BIRTH DATE</span><span class="fline" style="left:218px;top:73px;width:144px"></span>
    <span class="flabel" style="left:218px;top:85px">STREET ADDRESS</span><span class="fline" style="left:218px;top:98px;width:144px"></span>
    <span class="flabel" style="left:218px;top:112px">CITY</span><span class="fline" style="left:218px;top:125px;width:55px"></span>
    <span class="flabel" style="left:307px;top:112px">STATE</span><span class="fline" style="left:307px;top:125px;width:55px"></span>
    <span class="flabel" style="left:218px;top:136px">EMAIL</span><span class="fline" style="left:218px;top:149px;width:144px"></span>
    <span class="flabel" style="left:248px;top:160px;font-size:2.2px">○ I accept the Terms of Service and Privacy Statement</span>
    <span class="btn" style="left:272px;top:170px;width:37px;height:8px;font-size:4px">REGISTER</span>
  </div>
  <div class="close" style="top:43px"><svg width="16" height="16" viewBox="0 0 16 16"><path d="M4.5 4.5 11.5 11.5M11.5 4.5 4.5 11.5" stroke="#fff" stroke-width="1.4"/></svg></div>
</section>

</body>
</html>
```